Business Card Design

The image I attached was a quick thought to my design. I have triplets and was invisioning something with three figures with maybe the colors blue, pink and green. I would like it to look very chic and modern yet soothing/healing. I will take any fresh ideas as well.

Side 1: Contact Details
Side 2: Appointment section (mandatory)
Updates

Thank u all for your preliminary designs. I had sent the old design over and am looking for a bold fresh NEW LOOK  for CORE MOTION. I saw some really creative ideas in the gallery. If you have any other questions please feel free to email me at rtbwakes@quellmail.net.

Thanks

Please keep in mind that it is mandatory that on the back of the card is for appointments.

Thank you.

Reason: The two mandatory elements that need to be on the card is that her title needs to read as so:

Reason: The criteria is still not being met. Her title needs to read as so: Dr. Marisa Kettner, P.T., D.P.T. Doctor of Physical Therapy and The appointment info must go on the BACK of the card. Looking forward to some more great designs. Thanks.

Industry/Entity Type

Business

Contact Information for Business Card

Core Motion
Physical & Aquatic Therapy
Dr. Marisa Kettner, P.T., D.P.T.
Doctor of Physical Therapy

22-48 B Birchwick Lane
Elmbury, N.Y. 11592
(Located inside of the Summit gym in the Pinecrest shopping center)

Phone & Fax: (631) 555-0172
Mkettner4@harbornet.net

Requirements
Must have
• One the back I would like to do an appointment layout.

```html
<!DOCTYPE html>
<html lang="en">
<head>
<meta charset="utf-8">
<title>Core Motion Physical &amp; Aquatic Therapy – Business Card</title>
<link rel="stylesheet" href="https://fonts.googleapis.com/css2?family=Ubuntu:wght@400;500;700&family=Dancing+Script:wght@500&display=swap">
<style>
  :root {
    --bg: #e9ecef;
    --card: #f7f8f8;
    --ink: #1b2533;
    --blue: #3a9bd5;
    --blue-deep: #1f7fbf;
    --blue-light: #63bce8;
    --band-edge: #176aa3;
    --white: #ffffff;
  }
  * { box-sizing: border-box; margin: 0; padding: 0; }
  html, body {
    width: 1200px; height: 903px; overflow: hidden;
    background: var(--bg);
    font-family: "Ubuntu", sans-serif;
    color: var(--ink);
  }
  .canvas {
    position: relative; width: 1200px; height: 903px;
  }
  .card {
    position: absolute; left: 290px;
    width: 620px; height: 354px;
    background: var(--card);
    box-shadow: 0 6px 18px rgba(0,0,0,.18);
    overflow: hidden;
  }
  .card--back { top: 60px; }
  .card--front { top: 489px; }

  .card__heading {
    position: absolute; left: 40px; top: 30px;
    font-weight: 700; font-size: 29px; letter-spacing: -.2px;
    color: var(--ink);
  }
  .card__heading .accent { color: var(--blue); }

  .brand-mark {
    position: absolute; left: 44px; top: 120px;
    width: 200px; height: 150px;
    display: flex; align-items: center; gap: 12px;
  }
  .brand-mark__square {
    width: 30px; height: 30px; background: var(--blue); flex: none;
  }
  .brand-mark__name {
    font-weight: 700; font-size: 26px; color: var(--blue);
  }

  .band {
    position: absolute; left: 0; right: 0; bottom: 0; height: 58px;
    background: linear-gradient(90deg, var(--blue-deep), var(--blue-light));
    border-top: 3px solid var(--band-edge);
  }

  /* Back: appointment */
  .appointment {
    position: absolute; left: 290px; top: 130px; width: 290px;
  }
  .appointment__row {
    display: flex; align-items: flex-end; gap: 8px;
    font-weight: 700; font-size: 14px; height: 24px; margin-bottom: 42px;
  }
  .appointment__line {
    flex: 1; border-bottom: 1px solid #9aa5b1; height: 1px; margin-bottom: 3px;
  }

  /* Front: contact */
  .person {
    position: absolute; left: 300px; top: 92px;
  }
  .person__name {
    font-weight: 700; font-size: 20px;
    padding-bottom: 4px;
    border-bottom: 2px solid var(--blue);
    display: inline-block;
  }
  .person__title {
    font-family: "Dancing Script", cursive;
    font-size: 17px; color: #3c4756; margin-top: 4px;
  }
  .contact {
    position: absolute; left: 300px; top: 172px;
    list-style: none;
  }
  .contact__item {
    display: flex; align-items: center; gap: 10px;
    font-size: 18px; margin-bottom: 14px; color: var(--ink);
  }
  .contact__icon {
    width: 22px; height: 22px; border-radius: 3px;
    background: linear-gradient(180deg, var(--blue-light), var(--blue-deep));
    color: var(--white); font-size: 13px; font-weight: 500;
    display: flex; align-items: center; justify-content: center;
  }
  .address {
    position: absolute; left: 0; right: 0; bottom: 0; height: 58px;
    display: flex; flex-direction: column; justify-content: center;
    padding-left: 40px; color: var(--white);
  }
  .address__street { font-weight: 700; font-size: 14px; }
  .address__note { font-weight: 700; font-size: 11.5px; margin-top: 3px; }
</style>
</head>
<body>
<main class="canvas">

  <section class="card card--back" aria-label="Card back: appointment">
    <h1 class="card__heading"><span class="accent">Core Motion Physical</span> &amp; Aquatic Therapy</h1>
    <div class="brand-mark">
      <span class="brand-mark__square"></span>
      <span class="brand-mark__name">Core Motion</span>
    </div>
    <div class="appointment">
      <div class="appointment__row"><span>Appoinment Date:</span><span class="appointment__line"></span></div>
      <div class="appointment__row"><span>Appoinment Time:</span><span class="appointment__line"></span></div>
    </div>
    <div class="band"></div>
  </section>

  <section class="card card--front" aria-label="Card front: contact details">
    <h2 class="card__heading">Core Motion Physical &amp; Aquatic Therapy</h2>
    <div class="brand-mark">
      <span class="brand-mark__square"></span>
      <span class="brand-mark__name">Core Motion</span>
    </div>
    <div class="person">
      <div class="person__name">Dr. Marisa Kettner, P.T., D.P.T.</div>
      <div class="person__title">Doctor of Physical Therapy</div>
    </div>
    <ul class="contact">
      <li class="contact__item"><span class="contact__icon">P</span>(631) 555-0172</li>
      <li class="contact__item"><span class="contact__icon">e</span>Mkettner4@harbornet.net</li>
    </ul>
    <div class="band"></div>
    <div class="address">
      <div class="address__street">22-48 B Birchwick Lane Elmbury, N.Y. 11592</div>
      <div class="address__note">(Located inside of the Summit gym in the Pinecrest shopping center)</div>
    </div>
  </section>

</main>
</body>
</html>
```